Do me a Simple layout and Blow the stockings off my clients!!

I am a Personal Stylist focusing on helping women/mothers needing to revamp their wardrobe and feel confident and fresh again. I'm receiving very positive feedback and growing interest in the services I offer. I provide a 'Client Profile' as part of that service in a word document (saved as PDF). What I'm needing is to turn the average looking word document into a modern, funky and professional document template. I have a business logo and copy.
The template should be fluid, easy to update and communicate sassy, funky and professional.

Target Market(s)

Females 25-65.

Industry/Entity Type

Business

Font styles to use
Other font styles liked:
• HelveticaNeue Condensed, or Raleway

Requirements
Must have
• Colours and styles consistent with logo, and fashion industry.
• Interesting and emotive elements around the content.
• Create clear 'sections' with high impact (full coloured page with single, simple section heading ?)
Nice to have
• Ability to feature 'subjects' photos in interesting ways through out the document.
• Don't just stick with portrait layout, landscape is fine too.
Should not have
• Not too busy - less is more.

```html
<!DOCTYPE html>
<html lang="en">
<head>
<meta charset="utf-8">
<title>Client Profile – Totes to Stilettos</title>
<link href="https://fonts.googleapis.com/css2?family=Raleway:ital,wght@0,300;0,400;0,600;1,300;1,400&family=Questrial&display=swap" rel="stylesheet">
<style>
  :root{
    --pink:#ef4aa5;
    --pink-soft:#f7a6d2;
    --coral:#f28b86;
    --ink:#2b2b2b;
    --grey:#6d6d6d;
    --line:#d9d9d9;
    --backdrop:#e7e4e4;
    --paper:#ffffff;
  }
  *{box-sizing:border-box;margin:0;padding:0}
  html,body{width:849px;height:1200px;overflow:hidden}
  body{background:var(--backdrop);font-family:"Questrial",sans-serif;color:var(--ink);position:relative}

  .page{position:absolute;width:385px;height:556px;background:var(--paper);overflow:hidden}
  .page--cover{left:23px;top:29px}
  .page--report{left:441px;top:29px}
  .page--notes{left:23px;top:617px}
  .page--shop{left:441px;top:617px}

  .bar-top{position:absolute;left:0;right:0;top:0;height:11px;background:var(--pink)}
  .bar-bottom{position:absolute;left:0;right:0;bottom:0;height:8px;background:var(--pink)}

  /* brand lockup */
  .brand{position:absolute;text-align:right;font-family:"Raleway",sans-serif}
  .brand__name{color:var(--pink);font-weight:300;line-height:1}
  .brand__owner{color:var(--grey);font-weight:300;letter-spacing:.08em;text-transform:uppercase}
  .brand--large{left:95px;top:78px;width:190px}
  .brand--large .brand__name{font-size:36px}
  .brand--large .brand__owner{font-size:9px;margin-top:8px}
  .brand--small{right:12px;top:14px;width:120px}
  .brand--small .brand__name{font-size:20px}
  .brand--small .brand__owner{font-size:6px;margin-top:4px}

  /* cover */
  .cover-cloud{position:absolute;left:0;bottom:0;width:385px;height:176px}
  .cover-title{position:absolute;left:0;right:0;bottom:52px;text-align:center;color:#fff;
    font-family:"Raleway",sans-serif;font-weight:300;font-size:35px;letter-spacing:.02em}

  /* banners */
  .banner{position:absolute;left:0;background:var(--pink);color:#fff;border-radius:0 26px 26px 0;
    font-family:"Raleway",sans-serif;font-weight:400;text-transform:uppercase;display:flex;align-items:center;justify-content:center;text-align:center}
  .banner--report{top:34px;width:226px;height:48px;font-size:17px}
  .banner--notes{top:26px;width:256px;height:50px;font-size:14px;line-height:1.2}
  .banner--shop{top:23px;width:262px;height:42px;padding:0 14px;justify-content:flex-start;text-align:left;
    text-transform:none;font-style:italic;font-size:7.6px;line-height:1.4;font-weight:400}

  /* report */
  .report{position:absolute;left:23px;top:120px;width:330px;font-size:8.6px;line-height:1.6}
  .report dl{display:grid;grid-template-columns:58px 1fr;row-gap:1px}
  .report dt{color:var(--pink);font-weight:600;font-family:"Raleway",sans-serif}
  .report dd{font-weight:600;font-family:"Raleway",sans-serif}
  .report h3{color:var(--pink);font-family:"Raleway",sans-serif;font-weight:600;font-size:8.6px;margin-top:16px}
  .report ul{list-style:none;font-family:"Raleway",sans-serif;font-weight:600}
  .report li::before{content:"•"}
  .report li.indent{padding-left:4px}
  .report .gap{margin-top:40px}
  .report .celebs{margin-top:20px}

  /* notes */
  .note{position:absolute;left:23px;width:345px;display:flex;gap:14px}
  .note__frame{flex:0 0 102px;height:110px;border:1.5px solid var(--coral)}
  .note__text{font-style:italic;color:var(--grey);font-size:9.2px;line-height:1.5;padding-top:10px}
  .note:nth-of-type(1){top:117px}
  .note:nth-of-type(2){top:249px}
  .note:nth-of-type(3){top:380px}

  /* shop */
  .products{position:absolute;left:15px;top:114px;display:grid;grid-template-columns:178px 178px;grid-auto-rows:124px;column-gap:10px;row-gap:8px}
  .product{border:1.5px solid var(--pink);display:flex;padding:6px;gap:6px;background:#fff}
  .product__photo{flex:0 0 72px;height:100%}
  .product__info{font-size:5px;color:var(--grey);line-height:1.5;padding-top:4px}
  .product__name{font-family:"Raleway",sans-serif;font-weight:600;color:var(--ink);font-size:7px;text-transform:uppercase}
  .product__price{color:var(--ink);font-size:6px;margin-bottom:3px}
  .product__sizes{display:flex;gap:3px;margin:3px 0}
  .product__sizes span{width:8px;height:8px;border:.8px solid var(--line)}
  .product__cta{display:inline-block;margin-top:4px;background:var(--ink);color:#fff;padding:1px 5px;text-transform:uppercase}
  .tone-dress{background:linear-gradient(180deg,#f4f4f4 0%,#8a8a8a 45%,#f4f4f4 100%)}
  .tone-maxi{background:linear-gradient(160deg,#f5f5f5,#3c4150 60%,#eeeeee)}
  .tone-knit{background:linear-gradient(180deg,#f3f3f3,#8d8b88 50%,#f3f3f3)}
  .tone-blazer{background:linear-gradient(180deg,#f3f3f3,#9aa0a6 50%,#f1f1f1)}
  .tone-henley{background:linear-gradient(180deg,#f4f4f4,#b4b7bb 50%,#f4f4f4)}
  .tone-tee{background:linear-gradient(180deg,#f4f4f4,#2d3346 50%,#f4f4f4)}
</style>
</head>
<body>

<section class="page page--cover">
  <div class="bar-top"></div>
  <div class="brand brand--large">
    <div class="brand__name">Totes to<br>Stilettos</div>
    <div class="brand__owner">Lena Marlowe</div>
  </div>
  <svg class="cover-cloud" viewBox="0 0 385 176" aria-hidden="true">
    <path fill="#ef4aa5" d="M0 176 V62 Q0 44 18 44 H62 Q66 0 116 0 H269 Q319 0 323 44 H367 Q385 44 385 62 V176 Z"/>
  </svg>
  <h1 class="cover-title">CLIENT PROFILE</h1>
</section>

<section class="page page--report">
  <div class="bar-top" style="height:8px"></div>
  <h2 class="banner banner--report">Style Analysis Report</h2>
  <div class="brand brand--small">
    <div class="brand__name">Totes to<br>Stilettos</div>
    <div class="brand__owner">Lena Marlowe</div>
  </div>
  <div class="report">
    <dl>
      <dt>Client</dt><dd>: Jess</dd>
      <dt>Body Shape</dt><dd>: The Brick, shorter waist.</dd>
    </dl>
    <h3>Main characteristics:</h3>
    <ul>
      <li>Broad shoulders</li>
      <li>Hips inline with shoulders</li>
      <li>No shapely waist line</li>
      <li>Possibly larger (ish) thighs</li>
    </ul>
    <h3 class="gap">Main goals in dressing ‘The Brick’:</h3>
    <ul>
      <li>Create curves using shapely, flowing pieces</li>
      <li>Look for curved edges on garments</li>
      <li>Sweetheart necklines will instantly create a more shapely start to your upper body</li>
      <li>Use patterns to accentuate your best areas and detract from others.</li>
      <li>Use stripes of varying sizes, to create a shapely illusion</li>
      <li class="indent">For accessories look for curvy jewelry and handbags</li>
    </ul>
    <h3>Styles to avoid:</h3>
    <ul>
      <li>Square cut or boxed edge jackets</li>
      <li>Short skirts (mini) or shorts which will cut you off mid thigh</li>
      <li>Box pleats or pleats at the front of trousers</li>
      <li>Look for shoes that add to the flow of your garment, nothing too solid, or chunky</li>
    </ul>
    <dl class="celebs">
      <dt>Celebrity ‘Bricks’</dt><dd>&nbsp;: Mara Ellison, Tessa Quinn, Carla Brandt</dd>
    </dl>
  </div>
  <div class="bar-bottom"></div>
</section>

<section class="page page--notes">
  <div class="bar-top" style="height:8px"></div>
  <h2 class="banner banner--notes">Notes from<br>your styling session</h2>
  <div class="brand brand--small">
    <div class="brand__name">Totes to<br>Stilettos</div>
    <div class="brand__owner">Lena Marlowe</div>
  </div>
  <article class="note">
    <div class="note__frame"></div>
    <p class="note__text">Ok, I ’ll be short and sweet! Terrible! The sleeves do nothing for the tops of your arms, the seam across the middle of your waist is cutting you in two and the length of the top does nothing but draw attention to your crotch…thank goodness we put this one back on the hanger!</p>
  </article>
  <article class="note">
    <div class="note__frame"></div>
    <p class="note__text">Sophistication in a pair of heels! This outfit is so chic and elegant; it could be transformed from a work outfit to a daytime outfit, to a nighttime outfit, by changing up accessories. A jacket (eg, denim jacket or smart blazer) to a fabulous pairs of heels or a wedge! These trousers are great, look at how long and slender they make your legs look. They sit perfectly on your hips and then don’t cling anywhere. The straight/bootleg cut works really well for you. This outfit has to be a massive winner!</p>
  </article>
  <article class="note">
    <div class="note__frame"></div>
    <p class="note__text">Ok, I ’ll be short and sweet! Terrible! The sleeves do nothing for the tops of your arms, the seam across the middle of your waist is cutting you in two and the length of the top does nothing but draw attention to your crotch…thank goodness we put this one back on the hanger!</p>
  </article>
  <div class="bar-bottom"></div>
</section>

<section class="page page--shop">
  <div class="bar-top" style="height:8px"></div>
  <p class="banner banner--shop">I’ve also had quick surf on the net to see if there was anything worth looking at, or even just for you to use as a guide. I looked through Rue Velour, Marigold and Juno. These are just a few examples</p>
  <div class="brand brand--small">
    <div class="brand__name">Totes to<br>Stilettos</div>
    <div class="brand__owner">Lena Marlowe</div>
  </div>
  <div class="products">
    <div class="product">
      <div class="product__photo tone-dress" role="img" aria-label="Black and white wide stripe sleeveless dress"></div>
      <div class="product__info"><div class="product__name">Stripe knit dress</div><div class="product__price">$89.95</div>Soft jersey, fitted waist.<div class="product__sizes"><span></span><span></span><span></span><span></span></div>Size guide<br><span class="product__cta">Add to bag</span></div>
    </div>
    <div class="product">
      <div class="product__photo tone-maxi" role="img" aria-label="Navy and white diagonal stripe maxi dress"></div>
      <div class="product__info"><div class="product__name">Stripe maxi dress</div><div class="product__price">$129.95</div>Bias stripe, fluid drape.<div class="product__sizes"><span></span><span></span><span></span><span></span></div>Size guide<br><span class="product__cta">Add to bag</span></div>
    </div>
    <div class="product">
      <div class="product__photo tone-knit" role="img" aria-label="Grey marle slub knit jumper"></div>
      <div class="product__info"><div class="product__name">Slub knit</div><div class="product__price">$119.95</div>Relaxed crew, light marle.<div class="product__sizes"><span></span><span></span><span></span><span></span></div>Size guide<br><span class="product__cta">Add to bag</span></div>
    </div>
    <div class="product">
      <div class="product__photo tone-blazer" role="img" aria-label="Fine stripe grey blazer over a white top"></div>
      <div class="product__info"><div class="product__name">Stripe blazer</div><div class="product__price">$199.95</div>Tailored fit, soft shoulder.<div class="product__sizes"><span></span><span></span><span></span><span></span></div>Size guide<br><span class="product__cta">Add to bag</span></div>
    </div>
    <div class="product">
      <div class="product__photo tone-henley" role="img" aria-label="Grey fine stripe linen henley top"></div>
      <div class="product__info"><div class="product__name">Stripe linen henley</div><div class="product__price">$49.95</div>Scoop neck, rolled hem.<div class="product__sizes"><span></span><span></span><span></span><span></span></div>Size guide<br><span class="product__cta">Add to bag</span></div>
    </div>
    <div class="product">
      <div class="product__photo tone-tee" role="img" aria-label="Navy and white stripe sleeveless tee"></div>
      <div class="product__info"><div class="product__name">Mara stripe tee</div><div class="product__price">$59.95</div>Sleeveless, curved hem.<div class="product__sizes"><span></span><span></span><span></span><span></span></div>Size guide<br><span class="product__cta">Add to bag</span></div>
    </div>
  </div>
  <div class="bar-bottom"></div>
</section>

</body>
</html>
```